Web Design Project for Web Agency

WHAT I NEED:
The design I need (PSD file) is for a microsite designed for employee recruitment for Brantley, a Web agency.
***Design for the 1st Page ONLY : "Manifeste"
OBJECTIVES OF THE WEBSITE:
1. To promote the agency's corporate culture and HR management principles.
2. To get people to apply on available jobs
ELEMENTS OF THE PAGE "MANIFESTE" :
1. Brantley logo (see attached files). Beside the logo must be the word "Carrières" ("Careers" in english)
***The logo is not final and there is NO branding for Brantley yet. That is why there are multiple files. So please feel free to be creative!
2. Main menu : 4 sections
Manifeste | Opportunités | Brantly | Postuler
3. Manifeste :
This page is the home page. It will present 2 main sections :
a. The agency's corporate culture :
- Title of the page is a question : "Do you embrace Brantley's corporate culture?"
- Then, presentation of the 5 corporate values, each with a title and short description
- At the end of the list of values, we want a button that says "Apply now"
b. The agency's HR management principles :
- Title of the page is a question : "Do you see yourself working at Brantley?"
- Then, presentation of the 5 Management principles, each with a title and short description
- At the end of the list of principles, we want a button that says "Apply now"
VISUAL INSPIRATION
To create each section of the "Manifeste" page, we want a design that will fit with the corporate culture:
- Brantley is BOLD
- Brantley is PROUD
- Brantley is PROFESSIONAL
- Brantley is ELEGANT
- Brantley is REFINED
We want something slick and modern. Here are some Website's that we like that can be of inspiration:
- http://www.studio-vetrak.com/en/services
- http://quorvinpanels.com/

```html
<!DOCTYPE html>
<html lang="fr">
<head>
<meta charset="utf-8">
<title>Brantley Carrières — Manifeste</title>
<link rel="stylesheet" href="https://fonts.googleapis.com/css2?family=Jost:wght@300;400;600&family=Arimo:wght@400&display=swap">
<style>
:root{
  --orange:#ea6c2c;
  --orange-deep:#d85a1f;
  --orange-text:#b54716;
  --paper:#f1efea;
  --card:#f3f3f4;
  --card-line:#e0dfdd;
  --ink:#2b2b2b;
  --muted:#8a8a8a;
  --rule:#c9c7c2;
  --footer:#0b0b0b;
  --footer-text:#e9e9e9;
  --footer-muted:#9a9a9a;
}
*{margin:0;padding:0;box-sizing:border-box}
html,body{width:973px;height:1200px;overflow:hidden}
body{position:relative;background:var(--paper);font-family:"Arimo",Arial,sans-serif;color:var(--ink)}
.top-edge{position:absolute;left:0;top:0;width:973px;height:3px;background:repeating-linear-gradient(90deg,#333 0 3px,transparent 3px 5px)}
.abs{position:absolute}

/* header */
.brand{left:89px;top:34px}
.brand-name{font-family:"Jost",sans-serif;font-weight:600;font-size:44px;line-height:48px;color:var(--orange);letter-spacing:1px}
.brand-tag{font-family:"Jost",sans-serif;font-weight:400;font-size:10.5px;letter-spacing:4.6px;color:#555;margin-top:2px;padding-left:12px}
.social{left:742px;top:18px;display:flex;gap:11px}
.social span{width:27px;height:27px;border-radius:50%;background:var(--orange)}
.social span:nth-child(1){background:#2f4d97}
.social span:nth-child(2){background:#c9c9c9}
.social span:nth-child(3){background:#3ea6d8}
.main-nav{left:478px;top:80px;width:405px;height:28px;border-bottom:2px solid var(--rule)}
.main-nav a{position:absolute;top:3px;font-family:"Jost",sans-serif;font-size:12px;letter-spacing:.4px;color:#333;text-decoration:none}
.main-nav a.active{color:var(--orange)}
.main-nav .marker{position:absolute;left:30px;bottom:-6px;width:10px;height:10px;border-radius:50%;background:var(--orange)}

/* hero */
.hero{left:82px;top:122px;width:809px;height:330px;background:radial-gradient(ellipse at 50% 30%,#ee7a3c,#e5642a 70%,#dc5c22);box-shadow:0 18px 14px -14px rgba(0,0,0,.35);text-align:center;color:#fff}
.hero-title{position:absolute;left:0;right:0;top:40px;font-family:"Jost",sans-serif;font-weight:600;font-size:45px;letter-spacing:2.5px;text-shadow:0 2px 3px rgba(0,0,0,.3)}
.hero-sub{position:absolute;left:0;right:0;top:120px;font-family:"Jost",sans-serif;font-weight:300;font-size:27px;line-height:30px;letter-spacing:1px}
.hero-copy{position:absolute;left:180px;right:180px;top:208px;font-family:"Jost",sans-serif;font-size:14.6px;line-height:19.5px;letter-spacing:.6px;color:var(--orange-text)}
.hero-pager{position:absolute;left:360px;top:285px;width:90px;height:45px;border-radius:45px 45px 0 0;background:#f6f5f3}
.hero-pager svg{position:absolute;left:0;top:0}

/* section heading */
.section-head{left:87px;top:514px;width:803px;height:32px}
.section-head::before{content:"";position:absolute;left:0;right:0;top:16px;height:1px;background:var(--rule)}
.section-head h1{position:absolute;left:0;right:0;top:0;text-align:center;font-family:"Jost",sans-serif;font-weight:600;font-size:29px;line-height:32px;letter-spacing:1px;color:var(--orange)}
.section-head h1 span{background:var(--paper);padding:0 9px;position:relative}
.section-head i{position:absolute;top:11px;width:10px;height:10px;border-radius:50%;background:#7a7a7a}

/* cards */
.card{top:586px;width:393px;height:412px;background:var(--card);border:1px solid var(--card-line);box-shadow:0 0 0 3px #fbfaf8,0 1px 4px rgba(0,0,0,.12)}
.card h2{position:absolute;left:14px;top:14px;font-family:"Jost",sans-serif;font-weight:600;font-size:19.5px;color:var(--orange);white-space:nowrap}
.values{position:absolute;left:15px;top:53px;list-style:none}
.values li{position:relative;padding-left:21px;height:64px}
.values li::before{content:"»";position:absolute;left:0;top:-3px;font-size:15px;color:#888}
.values strong{display:block;font-weight:400;font-size:11.4px;line-height:14px;color:#222}
.values p{font-size:10.2px;line-height:14.6px;color:var(--muted);margin-top:2px;width:350px}
.apply{position:absolute;bottom:0;width:115px;height:35px;border-radius:50px 50px 0 0;background:linear-gradient(#f07a36,var(--orange-deep));color:#fff;font-family:"Jost",sans-serif;font-weight:600;font-size:15.4px;text-align:center;line-height:38px;text-decoration:none}

/* footer */
.site-footer{left:0;top:1036px;width:973px;height:164px;background:var(--footer)}
.site-footer::before{content:"";position:absolute;left:0;top:-4px;width:973px;height:5px;background:linear-gradient(135deg,var(--footer) 2.5px,transparent 2.5px) 0 0/5px 5px,linear-gradient(225deg,var(--footer) 2.5px,transparent 2.5px) 0 0/5px 5px}
.f-col{position:absolute;top:24px}
.f-col h3{font-family:"Jost",sans-serif;font-weight:400;font-size:11.4px;letter-spacing:.4px;color:var(--orange);margin-bottom:15px}
.f-col ul{list-style:none}
.f-col li{font-size:11px;line-height:24.5px;color:var(--footer-text);padding-left:14px;position:relative}
.f-col li::before{content:"";position:absolute;left:2px;top:10px;width:6px;height:6px;border-radius:50%;background:var(--orange)}
.f-col p{font-size:11px;line-height:18px;color:var(--footer-text)}
.f-brand{position:absolute;left:742px;top:22px;width:148px;text-align:center}
.f-brand .brand-name{font-size:34px;line-height:36px;color:#7d7d7d}
.f-brand .brand-tag{font-size:8px;letter-spacing:3px;color:#8a8a8a;padding-left:0}
.f-social{position:absolute;left:785px;top:95px;display:flex;gap:9px}
.f-social span{width:20px;height:20px;border-radius:50%;background:#6a6a6a}
.f-legal{position:absolute;right:83px;top:126px;text-align:right;font-size:10px;line-height:18px;color:var(--footer-muted)}
</style>
</head>
<body>
<div class="top-edge"></div>

<header>
  <div class="abs brand">
    <div class="brand-name">Brantley</div>
    <div class="brand-tag">AGENCE NUMÉRIQUE</div>
  </div>
  <div class="abs social" aria-label="Réseaux sociaux"><span></span><span></span><span></span><span></span></div>
  <nav class="abs main-nav">
    <a class="active" href="#" style="left:4px">MANIFESTE</a>
    <a href="#" style="left:113px">OPPORTUNITÉS</a>
    <a href="#" style="left:241px">BRANTLY</a>
    <a href="#" style="left:355px">POSTULER</a>
    <span class="marker"></span>
  </nav>
</header>

<section class="abs hero">
  <div class="hero-title">BRANTLEY IS PROFESSIONAL</div>
  <div class="hero-sub">THE BEST AND THE MOST EXPENSIVE<br>ARE NOT SYNONYMS</div>
  <p class="hero-copy">lorem Ipsum is simply dummy text of the printing and type-setting industry. Lorem Ipsum has been the industry's standard dummy text ever since the 1500s,</p>
  <div class="hero-pager">
    <svg width="90" height="45" viewBox="0 0 90 45">
      <line x1="45" y1="12" x2="45" y2="45" stroke="#d6d4d0"/>
      <polyline points="36,28 31,34 36,40" fill="none" stroke="#111" stroke-width="2.6"/>
      <polyline points="54,28 59,34 54,40" fill="none" stroke="#111" stroke-width="2.6"/>
    </svg>
  </div>
</section>

<div class="abs section-head">
  <i style="left:305px"></i>
  <h1><span>MANIFESTE</span></h1>
  <i style="left:488px"></i>
</div>

<article class="abs card" style="left:82px">
  <h2>The agency's corporate culture</h2>
  <ul class="values">
    <li><strong>Lorem Ipsum Dolor Sit Ametconst</strong><p>Aipisicing elit, sed do eiusmod temporincididunt ut labore et dolore magna aliqua. Utder enim ad minim veniam,</p></li>
    <li><strong>Lorem Ipsum Dolor Sit Ametconst</strong><p>Aipisicing elit, sed do eiusmod temporincididunt ut labore et dolore magna aliqua. Utder enim ad minim veniam,</p></li>
    <li style="height:62px"><strong>Lorem Ipsum Dolor Sit Ametconst</strong><p>Aipisicing elit, sed do eiusmod temporincididunt ut labore et dolore magna aliqua. Utder enim ad minim veniam,</p></li>
    <li><strong>Lorem Ipsum Dolor Sit Ametconst</strong><p>Aipisicing elit, sed do eiusmod temporincididunt ut labore et dolore magna aliqua. Utder enim ad minim veniam,</p></li>
    <li><strong>Lorem Ipsum Dolor Sit Ametconst</strong><p>Aipisicing elit, sed do eiusmod temporincididunt ut labore et dolore magna aliqua. Utder enim ad minim veniam,</p></li>
  </ul>
  <a class="apply" href="#" style="left:265px">Apply Now</a>
</article>

<article class="abs card" style="left:500px">
  <h2>The agency's HR management principles</h2>
  <ul class="values">
    <li><strong>Lorem Ipsum Dolor Sit Ametconst</strong><p>Aipisicing elit, sed do eiusmod temporincididunt ut labore et dolore magna aliqua. Utder enim ad minim veniam,</p></li>
    <li><strong>Lorem Ipsum Dolor Sit Ametconst</strong><p>Aipisicing elit, sed do eiusmod temporincididunt ut labore et dolore magna aliqua. Utder enim ad minim veniam,</p></li>
    <li style="height:62px"><strong>Lorem Ipsum Dolor Sit Ametconst</strong><p>Aipisicing elit, sed do eiusmod temporincididunt ut labore et dolore magna aliqua. Utder enim ad minim veniam,</p></li>
    <li><strong>Lorem Ipsum Dolor Sit Ametconst</strong><p>Aipisicing elit, sed do eiusmod temporincididunt ut labore et dolore magna aliqua. Utder enim ad minim veniam,</p></li>
    <li><strong>Lorem Ipsum Dolor Sit Ametconst</strong><p>Aipisicing elit, sed do eiusmod temporincididunt ut labore et dolore magna aliqua. Utder enim ad minim veniam,</p></li>
  </ul>
  <a class="apply" href="#" style="left:269px">Apply Now</a>
</article>

<footer class="abs site-footer">
  <div class="f-col" style="left:97px">
    <h3>VIEW SITE</h3>
    <ul><li>Manifeste</li><li>Opportunités</li><li>Brantly</li><li>Postuler</li></ul>
  </div>
  <div class="f-col" style="left:238px">
    <h3>HELP</h3>
    <ul><li>Help</li><li>Terms of Use</li><li>Privacy Policy</li><li>Cookies</li></ul>
  </div>
  <div class="f-col" style="left:358px">
    <h3>FIND US</h3>
    <p>412 Larkmoor Lane,<br>Eastvale, DC 52 Fr 52.</p>
  </div>
  <div class="f-col" style="left:524px">
    <h3>CONTACT</h3>
    <p style="padding-left:7px">Telephone: +1 800 555 0142<br>FAX: +1 800 555 0187</p>
  </div>
  <div class="f-brand">
    <div class="brand-name">Brantley</div>
    <div class="brand-tag">AGENCE NUMÉRIQUE</div>
  </div>
  <div class="f-social"><span></span><span></span><span></span><span></span></div>
  <div class="f-legal">Except where noted,<br>Copyright © 2012 Brantley Agence</div>
</footer>
</body>
</html>
```